Business Card Design

We have our logo and everything in place. Looking to have a layout for our new business cards designed. These will be printed with a matte finish, possibly rounded corners, and looking to incorporate some cool spot UV layers into the design.

Ive uploaded the existing card front and back as well as our logo.

Card Size Will Be 3.5" x 2"

```html
<!DOCTYPE html>
<html lang="en">
<head>
<meta charset="utf-8">
<title>Alder Deck and Rail — Business Cards</title>
<link href="https://fonts.googleapis.com/css2?family=Open+Sans:wght@400;600;700&display=swap" rel="stylesheet">
<style>
  :root {
    --backdrop: #e9e6e2;
    --silver-dark: #8c8c8c;
    --silver-mid: #c4c4c4;
    --silver-light: #f4f4f4;
    --ink: #111111;
    --ink-soft: #222222;
  }
  * { margin: 0; padding: 0; box-sizing: border-box; }
  html, body {
    width: 1200px; height: 900px; overflow: hidden;
    background: var(--backdrop);
    font-family: "Open Sans", Arial, sans-serif;
    color: var(--ink);
  }
  .canvas { position: relative; width: 1200px; height: 900px; }

  .card {
    position: absolute;
    border-radius: 16px;
    overflow: hidden;
    background: linear-gradient(115deg,
      var(--silver-dark) 0%, var(--silver-mid) 22%, var(--silver-light) 42%,
      #ffffff 50%, var(--silver-light) 58%, var(--silver-mid) 78%, var(--silver-dark) 100%);
    box-shadow: 0 6px 18px rgba(0,0,0,0.18);
  }
  .card-front { left: 78px; top: 35px; width: 587px; height: 362px; }
  .card-back  { left: 390px; top: 506px; width: 565px; height: 350px; }

  .wordmark {
    position: absolute;
    font-weight: 600;
    color: var(--ink);
    text-align: center;
    line-height: 1.1;
    white-space: nowrap;
  }
  .card-front .wordmark { left: 304px; top: 80px; width: 260px; font-size: 23px; }
  .card-back .wordmark  { left: 0; top: 150px; width: 565px; font-size: 44px; }

  .person { position: absolute; left: 40px; top: 193px; }
  .person-name { font-size: 19px; font-weight: 700; color: var(--ink); }
  .person-title { font-size: 15px; color: var(--ink-soft); margin-top: 1px; }

  .contacts { position: absolute; left: 40px; top: 263px; list-style: none; }
  .contacts li {
    display: flex; align-items: center; gap: 12px;
    font-size: 15px; color: var(--ink-soft); height: 22px;
  }
  .contacts svg { width: 11px; height: 11px; fill: var(--ink); flex: none; }
</style>
</head>
<body>
<main class="canvas">
  <section class="card card-front" aria-label="Card front">
    <div class="wordmark">Alder Deck and Rail</div>
    <div class="person">
      <div class="person-name">Marcus Ellery</div>
      <div class="person-title">President</div>
    </div>
    <ul class="contacts">
      <li>
        <svg viewBox="0 0 24 24" aria-hidden="true"><path d="M6.6 10.8a15.1 15.1 0 0 0 6.6 6.6l2.2-2.2a1 1 0 0 1 1-.25 11.4 11.4 0 0 0 3.6.57 1 1 0 0 1 1 1V20a1 1 0 0 1-1 1A17 17 0 0 1 3 4a1 1 0 0 1 1-1h3.5a1 1 0 0 1 1 1c0 1.25.2 2.45.57 3.57a1 1 0 0 1-.25 1z"/></svg>
        555.014.2290
      </li>
      <li>
        <svg viewBox="0 0 24 24" aria-hidden="true"><path d="M2 5h20v2l-10 7L2 7z"/><path d="M2 9l10 7 10-7v10H2z"/></svg>
        alderdeckandrail@mailbox.com
      </li>
      <li>
        <svg viewBox="0 0 24 24" aria-hidden="true"><circle cx="12" cy="12" r="10"/><path d="M2 12h20M12 2c3 3 3 17 0 20M12 2c-3 3-3 17 0 20" stroke="#e8e8e8" stroke-width="1.6" fill="none"/></svg>
        www.alderdeckandrail.com
      </li>
    </ul>
  </section>

  <section class="card card-back" aria-label="Card back">
    <div class="wordmark">Alder Deck and Rail</div>
  </section>
</main>
</body>
</html>
```